Web Design Project - Event Management Company

A web-page design needs to be created for an event management company. The logo has already been created, the design needs to draw on the themes and colors of the logo and extend on that.

The event management company likes to differentiate itself from others by being a bit "un-conventional" and being able to think outside the box.

the specialise in corporate events, weddings, AGMs, anything that requires coordination of resources. They also can provide Audio Visual services such as recording events.

final design will also require HTML implementation

```html
<!DOCTYPE html>
<html lang="en">
<head>
<meta charset="utf-8">
<title>Bright Box Group — Events</title>
<link href="https://fonts.googleapis.com/css2?family=PT+Sans:wght@400;700&family=PT+Sans+Narrow:wght@700&family=Ubuntu:wght@400;500;700&display=swap" rel="stylesheet">
<style>
  :root{
    --band-dark:#2c2c2c;
    --band-mid:#474747;
    --page:#f0f0f0;
    --white:#ffffff;
    --ink:#444444;
    --ink-soft:#777777;
    --heading:#333333;
    --orange:#e0541c;
    --amber:#cc6a12;
    --blue:#2a8fbf;
    --line:#dddddd;
    --panel:#f5f5f5;
    --pink-top:#fde6ee;
    --pink-bottom:#f6bfd1;
    --pink-ink:#a8888f;
  }
  *{box-sizing:border-box;margin:0;padding:0}
  html,body{width:1150px;height:1200px;overflow:hidden}
  body{
    position:relative;
    font-family:"PT Sans",Arial,sans-serif;
    color:var(--ink);
    background:linear-gradient(to bottom,var(--band-dark) 0,var(--band-mid) 166px,#e6e6e6 166px,var(--page) 260px,var(--page) 100%);
  }
  .abs{position:absolute}
  .sheet{left:86px;top:14px;width:978px;height:1018px;background:var(--white)}

  /* brand */
  .brand{left:98px;top:30px;width:220px;height:128px;text-align:center}
  .brand-mark{width:56px;height:56px;margin:12px auto 20px;background:var(--orange)}
  .brand-name{font-family:"PT Sans Narrow",sans-serif;font-weight:700;font-size:32px;line-height:34px;color:#333;white-space:nowrap}

  .phone{left:633px;top:59px;font-family:"Ubuntu",sans-serif;font-size:18px;color:var(--orange)}
  .search{left:826px;top:53px;width:227px;height:31px;border:1px solid var(--line);background:#fff;box-shadow:inset 0 1px 3px rgba(0,0,0,.08)}
  .search span{position:absolute;left:13px;top:7px;font-size:13px;color:#999}
  .search-btn{position:absolute;right:3px;top:3px;width:23px;height:23px;background:linear-gradient(#b4b4b4,#8a8a8a)}

  .nav{right:97px;top:136px;display:flex;font-family:"Ubuntu",sans-serif;font-size:14px;color:#555;white-space:nowrap}
  .nav a{color:inherit;text-decoration:none;padding:0 14px;border-left:1px solid var(--line);line-height:20px}
  .nav a:first-child{border-left:0}
  .nav a:last-child{padding-right:0}
  .nav a.active{color:var(--blue)}

  /* slider */
  .slider{left:95px;top:170px;width:960px;height:343px;background:#e2e2e2;padding:5px}
  .slide-photo{width:950px;height:333px;background:linear-gradient(to bottom,#c8ccd0 0,#d6d8da 30%,#7e96ad 55%,#5f7f9d 75%,#8ea4b5 100%)}
  .slide-title{left:599px;top:214px;font-family:"Ubuntu",sans-serif;font-weight:700;font-size:34px;color:var(--heading)}
  .slide-text{left:599px;top:264px;width:400px;font-size:13.5px;line-height:22px;color:#333}
  .slide-arrow{top:473px;width:20px;height:20px;background:#fff;border:1px solid #ccc}

  h2{position:absolute;font-family:"Ubuntu",sans-serif;font-weight:500;font-size:20px}
  .welcome-title{left:97px;top:537px;color:var(--orange)}
  .welcome-text{left:97px;top:574px;width:657px;font-size:14px;line-height:22px;text-align:justify}
  .rule{left:97px;top:725px;width:657px;border-top:2px dotted #999}
  .news-title{left:97px;top:745px;color:var(--amber)}
  .news-arrows{left:722px;top:750px}

  .card{top:780px;width:205px;height:241px;border:1px solid var(--line);background:#fff;padding:6px}
  .card-photo{width:191px;height:106px}
  .card h3{font-weight:400;font-size:14px;color:var(--amber);margin:11px 4px 4px}
  .card p{font-size:12.5px;line-height:18px;margin:0 4px;text-align:justify;color:#555}
  .card time{display:block;font-size:12.5px;color:#888;margin:8px 4px 0}

  .services-title{left:777px;top:537px;color:var(--blue)}
  .services{left:777px;top:579px;width:278px;height:346px;background:var(--panel);border:1px solid var(--line);padding:17px 0 0 20px;list-style:none}
  .services li{display:flex;align-items:center;height:36px;margin-top:-8px;margin-bottom:8px;font-size:14.5px;color:#444}
  .services svg{margin-right:12px}

  .callback{left:777px;top:938px;width:278px;height:83px;border:1px solid #eaa8bd;background:linear-gradient(var(--pink-top),var(--pink-bottom))}
  .callback-icon{position:absolute;left:30px;top:18px;width:44px;height:46px;background:#e9e4da;border:1px solid #cfc7b8}
  .callback small{position:absolute;left:86px;width:186px;top:6px;text-align:center;font-size:12px;color:#8c8c8c}
  .callback strong{position:absolute;left:86px;top:24px;width:186px;text-align:center;font-family:"Ubuntu",sans-serif;font-weight:500;font-size:21px;line-height:26px;color:var(--pink-ink)}

  .newsletter{left:86px;top:1046px;width:978px;height:60px;background:linear-gradient(#4c4c4c,#3c3c3c)}
  .newsletter-label{position:absolute;left:101px;top:15px;font-family:"Ubuntu",sans-serif;font-size:22px;color:#fff;white-space:nowrap}
  .newsletter-input{position:absolute;left:335px;top:14px;width:255px;height:32px;background:#fff;border:1px solid #ccc}
  .newsletter-input span{position:absolute;left:15px;top:8px;font-size:13px;color:#666}
  .newsletter-go{position:absolute;right:5px;top:3px;width:26px;height:26px;border-radius:50%;border:2px solid #c8c8c8}
  .bar-divider{position:absolute;left:645px;top:0;width:2px;height:60px;background:#2f2f2f;border-right:1px solid #5a5a5a}
  .social{position:absolute;top:14px;width:32px;height:32px;border-radius:3px;background:linear-gradient(#fafafa,#d6d6d6)}

  .footer-nav{left:0;top:1128px;width:1150px;text-align:center;font-size:14px;color:#333}
  .footer-nav span{padding:0 10px}
  .copyright{left:0;top:1160px;width:1150px;text-align:center;font-size:14px;color:#333}
</style>
</head>
<body>
  <div class="abs sheet"></div>

  <div class="abs brand">
    <div class="brand-mark"></div>
    <div class="brand-name">BRIGHT BOX GROUP</div>
  </div>

  <div class="abs phone">Call us : 555 012 7788</div>
  <div class="abs search"><span>Search</span><div class="search-btn"></div></div>

  <nav class="abs nav">
    <a class="active">Home</a><a>About us</a><a>Services</a><a>Resources</a><a>News &amp; Events</a><a>Contact us</a>
  </nav>

  <div class="abs slider">
    <div class="slide-photo" role="img" aria-label="Bride and groom standing on a beach by the sea"></div>
  </div>
  <div class="abs slide-title">Wedding Events</div>
  <p class="abs slide-text">Etiam ac augue in arcu tempus venenatis non id enim. Nullam ac dui sit amet dolor dapibus viverra a id orci. Sed sit amet lacus id tortor molestie sollicitudinAenean non lectus dapibus lacus.</p>
  <div class="abs slide-arrow" style="left:988px"><svg width="18" height="18" viewBox="0 0 18 18"><path d="M11 5 7 9l4 4" fill="none" stroke="#4a9a1e" stroke-width="2"/></svg></div>
  <div class="abs slide-arrow" style="left:1011px"><svg width="18" height="18" viewBox="0 0 18 18"><path d="M7 5l4 4-4 4" fill="none" stroke="#4a9a1e" stroke-width="2"/></svg></div>

  <h2 class="welcome-title">Welcome to Bright Box Group</h2>
  <p class="abs welcome-text">Nullam posuere mi mauris, vitae eleifend magna hendrerit facilisis. Praesent nunc felis, rutrum id arcu id, facilisis adipiscing leo. Praesent viverra mi in sem accumsan bibendum. Maecenas at mauris consequat, eleifend ligula vitae, pulvinar nisi. Proin ullamcorper lacinia leo nec luctus. Nulla ultricies dignissim mauris non viverra. Morbi non rhoncus tortor. In mollis leo luctus, iaculis mi ut, dictum libero. Donec sit amet ante sed diam eleifend lacinia sit amet non mauris. Nullam accumsan magna ultrices nulla tincidunt, vel ultricies lectus feugiat. Integer congue ligula nec lorem rhoncus rhoncus.</p>
  <div class="abs rule"></div>

  <h2 class="news-title">Latest News and Events</h2>
  <svg class="abs news-arrows" width="30" height="16" viewBox="0 0 30 16"><path d="M8 3 3 8l5 5M20 3l5 5-5 5" fill="none" stroke="#555" stroke-width="2"/></svg>

  <article class="abs card" style="left:98px">
    <div class="card-photo" role="img" aria-label="Crowd at a concert with stage lights" style="background:linear-gradient(#3a1a2a,#7a2a1a 60%,#b0461e)"></div>
    <h3>Donec pellentesque euismo</h3>
    <p>Aenean porttitor, tellus ac sollici tudin facilisis, est lacus rhoncus libero, eu vestibulum tortor.</p>
    <time>Aug-1-13</time>
  </article>
  <article class="abs card" style="left:322px">
    <div class="card-photo" role="img" aria-label="Conference hall with rows of seats and a lit stage" style="background:linear-gradient(#1a1a1e,#4a2a24 55%,#6a4a3a)"></div>
    <h3>Donec pellentesque euismo</h3>
    <p>Aenean porttitor, tellus ac sollici tudin facilisis, est lacus rhoncus libero, eu vestibulum tortor.</p>
    <time>Aug-1-13</time>
  </article>
  <article class="abs card" style="left:545px">
    <div class="card-photo" role="img" aria-label="Banquet room with round dining tables set for an event" style="background:linear-gradient(#8a6a4a,#c89a6a 50%,#d8c4b0)"></div>
    <h3>Donec pellentesque euismo</h3>
    <p>Aenean porttitor, tellus ac sollici tudin facilisis, est lacus rhoncus libero, eu vestibulum tortor.</p>
    <time>Aug-1-13</time>
  </article>

  <h2 class="services-title">Our Services</h2>
  <ul class="abs services">
    <li><svg width="7" height="10" viewBox="0 0 7 10"><path d="M1 1l4 4-4 4" fill="none" stroke="#777" stroke-width="1.6"/></svg>Fusce at pharetra nulla</li>
    <li><svg width="7" height="10" viewBox="0 0 7 10"><path d="M1 1l4 4-4 4" fill="none" stroke="#777" stroke-width="1.6"/></svg>Praesent nunc felis</li>
    <li><svg width="7" height="10" viewBox="0 0 7 10"><path d="M1 1l4 4-4 4" fill="none" stroke="#777" stroke-width="1.6"/></svg>Aenean non lectus dapibus</li>
    <li><svg width="7" height="10" viewBox="0 0 7 10"><path d="M1 1l4 4-4 4" fill="none" stroke="#777" stroke-width="1.6"/></svg>Nunc sitamet</li>
    <li><svg width="7" height="10" viewBox="0 0 7 10"><path d="M1 1l4 4-4 4" fill="none" stroke="#777" stroke-width="1.6"/></svg>Nullam gravida gravida</li>
    <li><svg width="7" height="10" viewBox="0 0 7 10"><path d="M1 1l4 4-4 4" fill="none" stroke="#777" stroke-width="1.6"/></svg>Mauris aliquam vulputate</li>
    <li><svg width="7" height="10" viewBox="0 0 7 10"><path d="M1 1l4 4-4 4" fill="none" stroke="#777" stroke-width="1.6"/></svg>Donec vitae</li>
    <li><svg width="7" height="10" viewBox="0 0 7 10"><path d="M1 1l4 4-4 4" fill="none" stroke="#777" stroke-width="1.6"/></svg>Nullam vel rutrum dui</li>
    <li><svg width="7" height="10" viewBox="0 0 7 10"><path d="M1 1l4 4-4 4" fill="none" stroke="#777" stroke-width="1.6"/></svg>Suspendisse sit amet</li>
  </ul>

  <div class="abs callback">
    <div class="callback-icon" role="img" aria-label="Notepad with pencil illustration"></div>
    <small>Click herer for</small>
    <strong>REQUEST A CALL BACK</strong>
  </div>

  <div class="abs newsletter">
    <svg style="position:absolute;left:42px;top:15px" width="38" height="28" viewBox="0 0 38 28"><rect x="1.5" y="1.5" width="35" height="25" fill="none" stroke="#fff" stroke-width="3"/><path d="M2 3l17 14L36 3M2 26l12-11M36 26 24 15" fill="none" stroke="#fff" stroke-width="3"/></svg>
    <div class="newsletter-label">Newsletter Subscribe</div>
    <div class="newsletter-input"><span>Enter your email ID</span><div class="newsletter-go"></div></div>
    <div class="bar-divider"></div>
    <div class="social" style="left:682px"></div>
    <div class="social" style="left:737px"></div>
    <div class="social" style="left:792px"></div>
    <div class="social" style="left:847px"></div>
    <div class="social" style="left:902px"></div>
  </div>

  <div class="abs footer-nav"><span>Home</span>|<span>About us</span>|<span>Services</span>|<span>Resources</span>|<span>News &amp; Events</span>|<span>Contact us</span></div>
  <div class="abs copyright">Copyright &copy; 2013 &nbsp;Bright Box Group. &nbsp;&nbsp;All rights reserved.</div>
</body>
</html>
```